HVAC company business card design

We need a business card design for a HVAC company. The design must look professional. Both sides will be used. The total data to be on the business card is
Name
Position
Email
Direct Phone/Moile Phone
Company Contacts /Address, Phone, Fax, web)
All data will be submit once the design is confirmed. For generic purposes use;
Emre Toksoy
Managing Director
+902324815263 (Mobile)
4712 Sokak No: 9 KBSE Yenikent IZMIR TURKEY
Tel: +902324815263 Fax : +902324815269
www.luvon.com.tr

Target Market(s)

HVAC

Industry/Entity Type

Business

Contact Information for Business Card

The total data to be on the business card is
Name
Position
Email
Direct Phone/Moile Phone
Emre Toksoy
Managing Director
+902324815263 (Mobile)
www.luvon.com.tr
The BC will use both sides of the card. The front will include the full logo and the details for the business card holder. The business card can be divided into vertical/horizontal or to a special shape. The common data like the company address/phone/fax should be indicated elsewehere. The back can contain some part or the whole logo and must contain the web address.

Font styles to use
Serif
Sans Serif

Colors
0355a3
cfdfed

Requirements
Should not have
• Please be careful with the fonts, it shouldnt be too small or too big and must not interfere with the logo fonts. If you need to use a curvy shape please do not use as the logo is already curvy or use the curves from the logo (if it looks good, otherwise forget it)
• We are not in favor of pictograms, only if they are perfect use them.

```html
<!DOCTYPE html>
<html lang="en">
<head>
<meta charset="utf-8">
<title>LUVON business card</title>
<link href="https://fonts.googleapis.com/css2?family=Montserrat:wght@300;400;600&display=swap" rel="stylesheet">
<style>
  :root{
    --bg:#cfe8e0;
    --card-black:#030303;
    --blue-light:#2f9cc6;
    --blue-mid:#17598a;
    --blue-deep:#0f3a66;
    --brand-blue:#0355a3;
    --brand-soft:#cfdfed;
    --logo-text:#3a4f86;
    --white:#ffffff;
    --icon-dark:#1e2328;
    --split:282px;
  }
  *{margin:0;padding:0;box-sizing:border-box}
  html,body{width:1200px;height:856px;overflow:hidden;background:var(--bg)}
  body{font-family:"Montserrat",Arial,sans-serif;color:var(--white);position:relative}
  .card{
    position:absolute;left:294px;width:612px;height:360px;border-radius:34px;
    overflow:hidden;background:var(--card-black);box-shadow:0 10px 26px rgba(0,60,60,.18);
  }
  .card--front{top:48px}
  .card--back{top:448px}

  .brand{display:flex;align-items:center;gap:14px}
  .brand__mark{border-radius:50%;background:var(--brand-blue);flex:none}
  .brand__name{font-weight:600;color:var(--logo-text);letter-spacing:.06em;line-height:1;white-space:nowrap}

  /* front */
  .front__holder{position:absolute;left:0;top:0;width:var(--split);height:100%;padding:46px 0 0 36px}
  .front__holder .brand__mark{width:46px;height:46px}
  .front__holder .brand__name{font-size:33px}
  .holder__name{position:absolute;left:36px;top:180px;font-size:27px;font-weight:300;letter-spacing:.01em;white-space:nowrap}
  .holder__role{position:absolute;left:36px;top:222px;font-size:16px;font-weight:400;white-space:nowrap}
  .holder__mobile{position:absolute;left:36px;top:290px;display:flex;align-items:center;gap:12px;font-size:16px;white-space:nowrap}

  .front__company{
    position:absolute;left:var(--split);top:0;right:0;bottom:0;padding:42px 0 0 40px;
    background:radial-gradient(circle at 48% 48%,var(--blue-light) 0%,var(--blue-mid) 45%,var(--blue-deep) 100%);
  }
  .company__address{font-size:16px;line-height:1.3;font-weight:400}
  .company__contacts{position:absolute;left:40px;top:210px;list-style:none}
  .company__contacts li{display:flex;align-items:center;gap:12px;font-size:16px;margin-bottom:10px;white-space:nowrap}
  .icon{width:26px;height:26px;border-radius:50%;background:var(--icon-dark);display:flex;align-items:center;justify-content:center;flex:none}
  .icon--light{background:var(--white)}
  .icon svg{width:15px;height:15px}

  /* back */
  .back__brand{position:absolute;inset:0;justify-content:center}
  .back__brand .brand__mark{width:86px;height:86px}
  .back__brand .brand__name{font-size:66px}
</style>
</head>
<body>

<section class="card card--front" aria-label="Card front">
  <div class="front__holder">
    <div class="brand">
      <span class="brand__mark"></span>
      <span class="brand__name">LUVON</span>
    </div>
    <p class="holder__name">EMRE TOKSOY</p>
    <p class="holder__role">Managing Director</p>
    <p class="holder__mobile">
      <span class="icon">
        <svg viewBox="0 0 16 16"><rect x="4" y="1.5" width="8" height="13" rx="1.5" fill="none" stroke="#fff" stroke-width="1.4"/><circle cx="8" cy="12" r=".8" fill="#fff"/></svg>
      </span>
      +902324815263
    </p>
  </div>

  <div class="front__company">
    <p class="company__address">4712 Sokak No: 9<br>KBSE Yenikent<br>IZMIR TURKEY</p>
    <ul class="company__contacts">
      <li>
        <span class="icon icon--light"><svg viewBox="0 0 16 16"><path d="M4 2l2.5 3-1.3 1.6c.8 1.7 2 2.9 3.6 3.6L10.4 9 13.5 11.5 12 14C7 13.5 2.5 9 2 4z" fill="#111"/></svg></span>
        +902324815263
      </li>
      <li>
        <span class="icon icon--light"><svg viewBox="0 0 16 16"><rect x="3" y="2" width="8" height="5" fill="none" stroke="#111" stroke-width="1.3"/><rect x="2" y="7" width="12" height="7" rx="1" fill="#111"/></svg></span>
        +902324815269
      </li>
      <li>
        <span class="icon icon--light"><svg viewBox="0 0 16 16"><g fill="none" stroke="#111" stroke-width="1.2"><circle cx="8" cy="8" r="6"/><ellipse cx="8" cy="8" rx="2.6" ry="6"/><path d="M2 8h12M3 5h10M3 11h10"/></g></svg></span>
        www.luvon.com.tr
      </li>
    </ul>
  </div>
</section>

<section class="card card--back" aria-label="Card back">
  <div class="brand back__brand">
    <span class="brand__mark"></span>
    <span class="brand__name">LUVON</span>
  </div>
</section>

</body>
</html>
```